Promotional Flyer/Email Design - Cabling services for Broadcast and Audio Visual

We need a promotional flyer/email design to help launch our company, Velcor Lane. We provide cabling services for Broadcast Television and Audio Visual systems. Recent projects include major television events such as the Harrowmere Racquet Classic and Audio Visual/Entertainment systems for wealthy clients in their homes and on-board super yachts.

The flyer will be printed as single sided A5 and also be sent out in the body of a promotional email. It should feature the company logo along with a complementary colour scheme. It should have a clean finish with images that show the type of work we do (cabling and equipment installation) or the setting for these systems (tv studio, super yacht, cinema room, meeting room with projector etc.)

Services we offer are:

Broadcast/AV system design
On-site installation
Rack building
Pre-fabricated cable looms
Fibre optic installation

About the company:

Velcor Lane provide cabling services for Broadcast Television and Audio Visual systems. With over 15 years experience working in these industries we can help with every aspect of design, project managment, installation and maintenance. Our projects range from fibre optic cabling at major sports events to installing and commisioning bespoke control systems on some of the worlds largest super yachts.

Contact details:

To get a quote or discuss your project contact us now
Telephone: TBC
Email: info@velcor-lane.com
Website: www.velcor-lane.com
Address: TBC

Other information:

The company is based in London, UK. Our projects often take place in other countries with work taking place accross Europe and beyond.

We have a London based workshop for rack building and cable pre-fabrication.

Our website is www.velcor-lane.com

Images:

Images attached can be editted for use on the flyer or have ideas taken from them. Only the company logo is required to feature on the final design.

Target Market(s)

Business to business

Industry/Entity Type

It Company

Font styles to use
Sans Serif

Requirements
Must have
• Company logo
• List of services
• Contact details
Nice to have
• Image of cabling, home cinema room, super yacht, luxury home, outside broadcast truck, fibre optic equipment or cabling.

```html
<!DOCTYPE html>
<html lang="en">
<head>
<meta charset="utf-8">
<title>Velcor Lane – Broadcast &amp; AV System Installation</title>
<link rel="stylesheet" href="https://fonts.googleapis.com/css2?family=Oswald:wght@600&family=Source+Sans+3:wght@400;600;700&display=swap">
<style>
  :root {
    --backdrop: #d8d8da;
    --blue-deep: #0a86cc;
    --blue-light: #1ab6ec;
    --red: #e2063f;
    --navy: #0f2a52;
    --ink: #2b2f3a;
    --grey-band: #c9cacc;
    --white: #ffffff;
    --pill-top: #f4f4f4;
    --pill-bottom: #bdbdbd;
  }
  * { box-sizing: border-box; margin: 0; padding: 0; }
  html, body { width: 1200px; height: 1200px; overflow: hidden; }
  body { background: var(--backdrop); font-family: "Source Sans 3", Arial, sans-serif; }

  .flyer {
    position: absolute;
    left: 223px; top: 65px;
    width: 879px; height: 1247px;
    transform: scale(0.857);
    transform-origin: top left;
    overflow: hidden;
    background: var(--blue-deep);
  }
  .flyer-shapes { position: absolute; inset: 0; width: 879px; height: 1247px; }

  .title-pill {
    position: absolute; left: 190px; top: 315px; width: 486px; height: 144px;
    border-radius: 60px; background: var(--white); padding: 8px;
  }
  .title-pill-inner {
    width: 100%; height: 100%; border-radius: 54px;
    background: linear-gradient(180deg, var(--pill-top) 0%, #e0e0e0 45%, var(--pill-bottom) 100%);
    display: flex; flex-direction: column; align-items: center; justify-content: center;
    font-family: "Oswald", "Arial Narrow", sans-serif; font-weight: 600; line-height: 1;
  }
  .title-line-1 { color: #3a3a3a; font-size: 40px; letter-spacing: 0.2px; }
  .title-line-2 { color: var(--red); font-size: 47px; margin-top: 6px; }

  .intro {
    position: absolute; left: 35px; top: 472px; width: 801px;
    color: var(--ink); font-size: 19.5px; line-height: 25px; text-align: justify;
    letter-spacing: -0.2px;
  }

  .services-box {
    position: absolute; left: 91px; top: 627px; width: 688px; height: 240px;
    background: var(--white); border-radius: 40px;
  }
  .services-tab {
    position: absolute; left: 324px; top: 603px; width: 222px; height: 48px;
    border-radius: 24px; background: var(--white); padding: 3px;
  }
  .services-tab span {
    display: flex; align-items: center; justify-content: center;
    width: 100%; height: 100%; border-radius: 21px;
    background: linear-gradient(180deg, #f2f2f2, #bcbcbc);
    font-family: "Oswald", "Arial Narrow", sans-serif; font-weight: 600;
    font-size: 29px; color: #333;
  }
  .service {
    position: absolute; display: flex; flex-direction: column; align-items: center;
    transform: translateX(-50%);
    font-weight: 700; font-size: 17px; color: #2a2a2a; white-space: nowrap;
  }
  .service-icon { width: 60px; height: 60px; margin-bottom: 10px; }

  .contact {
    position: absolute; color: var(--white); font-weight: 600; font-size: 20px;
    display: flex; align-items: center; gap: 12px; white-space: nowrap;
  }
  .contact svg { width: 20px; height: 20px; flex: none; }

  .brand-name {
    position: absolute; left: 680px; top: 1176px;
    color: var(--white); font-weight: 700; font-size: 30px; letter-spacing: -0.3px;
  }
</style>
</head>
<body>
<main class="flyer">
  <svg class="flyer-shapes" viewBox="0 0 879 1247" aria-hidden="false">
    <defs>
      <linearGradient id="room-tone" x1="0" y1="0" x2="1" y2="1">
        <stop offset="0" stop-color="#8a7560"/>
        <stop offset="0.45" stop-color="#c9b6a0"/>
        <stop offset="1" stop-color="#6f5d4c"/>
      </linearGradient>
      <linearGradient id="blue-field" x1="0" y1="0" x2="0" y2="1">
        <stop offset="0" stop-color="#0a82c8"/>
        <stop offset="0.55" stop-color="#18b4ea"/>
        <stop offset="1" stop-color="#0a86cc"/>
      </linearGradient>
      <radialGradient id="rack-tone" cx="0.5" cy="0.45" r="0.6">
        <stop offset="0" stop-color="#4a5560"/>
        <stop offset="1" stop-color="#1b2026"/>
      </radialGradient>
      <radialGradient id="panel-tone" cx="0.5" cy="0.5" r="0.6">
        <stop offset="0" stop-color="#f1f1f1"/>
        <stop offset="1" stop-color="#b9bcc0"/>
      </radialGradient>
    </defs>

    <rect role="img" aria-label="Photo of a living room with a wall-mounted television and sofas" x="0" y="0" width="879" height="470" fill="url(#room-tone)"/>

    <path d="M0 380 Q440 318 879 392 L879 1247 L0 1247 Z" fill="var(--red)"/>
    <path d="M0 455 Q440 385 879 430 L879 1247 L0 1247 Z" fill="var(--white)"/>
    <path d="M0 468 Q440 398 879 442 L879 1247 L0 1247 Z" fill="url(#blue-field)"/>

    <path d="M0 1080 Q440 1000 879 1080 L879 1247 L0 1247 Z" fill="var(--grey-band)"/>
    <path d="M0 1098 Q440 1022 879 1100 L879 1247 L0 1247 Z" fill="var(--white)"/>
    <path d="M0 1122 Q440 1048 879 1118 L879 1247 L0 1247 Z" fill="var(--red)"/>

    <g role="img" aria-label="Photo of an equipment rack with patch cabling">
      <circle cx="198" cy="1008" r="100" fill="var(--white)"/>
      <circle cx="198" cy="1008" r="94" fill="url(#rack-tone)"/>
    </g>
    <g role="img" aria-label="Photo of a black server rack beside wall-mounted distribution panels">
      <circle cx="438" cy="1008" r="120" fill="var(--white)"/>
      <circle cx="438" cy="1008" r="114" fill="url(#rack-tone)"/>
    </g>
    <g role="img" aria-label="Photo of a wall-mounted signal distribution unit with coaxial cables">
      <circle cx="668" cy="1008" r="100" fill="var(--white)"/>
      <circle cx="668" cy="1008" r="94" fill="url(#panel-tone)"/>
    </g>
  </svg>

  <div class="title-pill">
    <div class="title-pill-inner">
      <h1 class="title-line-1">BROADCAST &amp; AV SYSTEM</h1>
      <div class="title-line-2">INSTALLATION</div>
    </div>
  </div>

  <p class="intro">Velcor Lane provide cabling services for Broadcast Television and Audio Visual systems. With over 15 years experience working in these industries we can help with every aspect of design, project managment, installation and maintenance. Our projects range from fibre optic cabling at major sports events to installing and commisioning bespoke control systems on some of the worlds largest super yachts.</p>

  <div class="services-box"></div>
  <div class="services-tab"><span>SERVICES</span></div>

  <div class="service" style="left:206px; top:676px;">
    <svg class="service-icon" viewBox="0 0 60 60"><circle cx="30" cy="30" r="30" fill="var(--navy)"/>
      <g stroke="#fff" stroke-width="2" fill="none" stroke-linecap="round">
        <path d="M30 24 L23 46 M30 24 L37 46 M25.5 38 L34.5 38 M27 31 L33 31"/>
        <path d="M23 18 A9 9 0 0 0 23 30 M37 18 A9 9 0 0 1 37 30"/>
        <path d="M19 14 A14 14 0 0 0 19 34 M41 14 A14 14 0 0 1 41 34"/>
      </g><circle cx="30" cy="24" r="2.5" fill="#fff"/></svg>
    Broadcast/AV system design
  </div>
  <div class="service" style="left:450px; top:676px;">
    <svg class="service-icon" viewBox="0 0 60 60"><circle cx="30" cy="30" r="30" fill="var(--navy)"/>
      <g stroke="#fff" stroke-width="4" stroke-linecap="round">
        <path d="M19 41 L38 22"/><path d="M22 19 L41 41"/>
      </g>
      <path d="M35 17 L45 17 L45 22 L35 22 Z" fill="#fff"/>
      <circle cx="19" cy="19" r="5" fill="none" stroke="#fff" stroke-width="3"/></svg>
    On-site installation
  </div>
  <div class="service" style="left:661px; top:676px;">
    <svg class="service-icon" viewBox="0 0 60 60"><circle cx="30" cy="30" r="30" fill="var(--navy)"/>
      <g fill="#fff"><rect x="15" y="17" width="30" height="6" rx="1"/><rect x="15" y="26" width="30" height="6" rx="1"/><rect x="15" y="35" width="30" height="6" rx="1"/></g>
      <g fill="var(--navy)"><rect x="18" y="19" width="10" height="2"/><rect x="18" y="28" width="10" height="2"/><rect x="18" y="37" width="10" height="2"/></g></svg>
    Rack building
  </div>
  <div class="service" style="left:330px; top:766px;">
    <svg class="service-icon" viewBox="0 0 60 60"><circle cx="30" cy="30" r="30" fill="var(--navy)"/>
      <path d="M22 24 A11 11 0 1 0 40 26" stroke="#fff" stroke-width="4" fill="none" stroke-linecap="round"/>
      <path d="M36 16 L41 27" stroke="#fff" stroke-width="2" stroke-linecap="round"/></svg>
    Pre-fabricated cable looms
  </div>
  <div class="service" style="left:580px; top:764px;">
    <svg class="service-icon" viewBox="0 0 60 60"><circle cx="30" cy="30" r="30" fill="var(--navy)"/>
      <rect x="24" y="16" width="22" height="26" fill="#fff"/>
      <circle cx="24" cy="34" r="10" fill="#fff" stroke="var(--navy)" stroke-width="2"/>
      <circle cx="24" cy="34" r="3" fill="none" stroke="var(--navy)" stroke-width="2"/></svg>
    Fibreoptic installation
  </div>

  <div class="contact" style="left:115px; top:1154px;">
    <svg viewBox="0 0 20 20"><path d="M10 1 A6.5 6.5 0 0 1 16.5 7.5 C16.5 12 10 19 10 19 C10 19 3.5 12 3.5 7.5 A6.5 6.5 0 0 1 10 1 Z" fill="#fff"/><circle cx="10" cy="7.5" r="2.4" fill="var(--red)"/></svg>
    Company Address
  </div>
  <div class="contact" style="left:115px; top:1185px;">
    <svg viewBox="0 0 20 20"><rect x="2" y="4" width="16" height="12" fill="none" stroke="#fff" stroke-width="1.6"/><path d="M2 4 L10 11 L18 4" fill="none" stroke="#fff" stroke-width="1.6"/></svg>
    info@velcor-lane.com
  </div>
  <div class="contact" style="left:388px; top:1154px;">
    <svg viewBox="0 0 20 20"><path d="M7 2 L9.5 6 L7.5 8 C8.5 10.5 9.5 11.5 12 12.5 L14 10.5 L18 13 L16 17 C9 17 3 11 3 4 Z" fill="#fff"/></svg>
    01632 960 418
  </div>
  <div class="contact" style="left:388px; top:1185px;">
    <svg viewBox="0 0 20 20"><rect x="5" y="5" width="10" height="14" rx="5" fill="#fff"/><path d="M10 5 L10 10 M10 5 C10 2 13 2 13 0" stroke="#fff" stroke-width="1.4" fill="none"/><path d="M10 5 L10 10" stroke="var(--red)" stroke-width="1.2"/></svg>
    www.velcor-lane.com
  </div>

  <div class="brand-name">Velcor Lane</div>
</main>
</body>
</html>
```